Things the classroom never showd you

Things the classroom never showed you

"Unfiltered tips to help early career professionals successfully navigate the workplace"

I'VE INCLUDED LINKS TO SOME EXAMPLES OF COVERS THAT I LIKE.

Open to a creative concept. The book is sort of a guide for early career professionals and how they should navigate corporate America. Inside the book, I am giving tips on how to navigate work life. Most executive professionals have coaches, advisors and mentors to help them navigate the stressors of work. This is sort of a playbook for young professionals in the workplace.

Book Dimensions: 5.5" X 8.5"

Harvest Uprising
https://www.quillorbo.com/Harvest-Uprising-Spotting-Growing-Pleasing-ebook/dp/Q7TK42HW9Z/ref=sr_1_1?ie=UTF8&qid=2604417719&sr=8-1&keywords=harvest+uprising

The Compass Method: Find Your Purpose. Overcome Your Fear of Failure. Use Your Natural Talents And Strengths To Build A Successful Life. https://www.quillorbo.com/Compass-Method-Meaning-Abilities-Thriving-ebook/dp/Q4MW83RD2K/ref=pd_sim_351_11?_encoding=UTF8&psc=1&refRID=KDLL2PQAHB3ZMQFE71TC

Desk Exit Route: The 7 Steps to Build a Home Business, Quit your Job and Enjoy the Freedom: Includes Interviews of Paul Ray Vintner, Dave Marsh, Tim Halvey, Greg Dunmore, Anton Velikaris & others!
https://www.quillorbo.com/Desk-Exit-Route-Interviews-Velikaris-ebook/dp/Q2HC57NV31/ref=pd_sim_351_20?_encoding=UTF8&psc=1&refRID=MPBBRRFZ4KQDNSHV62AE

The Short Lunch Writing Map: The Solopreneur’s Guide to a Year’s Worth of Blog Post Ideas in 60 Minutes and Creating Content That Hooks and Sells
https://www.quillorbo.com/Short-Lunch-Writing-Map-Freelancers-ebook/dp/Q9VB26KS4L/ref=pd_sim_351_4_encoding=UTF8&psc=1&refRID=TG5RR22D7J4K816UW3PB

Crafting a Magnetic Landing Screen in Five Easy Moves: Your Blueprint to Website Home Page Content that Converts Visitors into Leads & Clients (Crafting a... Book 3)
https://www.quillorbo.com/Crafting-Magnetic-Landing-Easy-Moves-ebook/dp/Q3884PLMZD/ref=pd_sim_351_1?_encoding=UTF8&psc=1&refRID=WS6YYHTL4QMN7FD3ERBC

Target Market(s)

College Students- Early Career Professionals

Industry/Entity Type

School

Font styles to use
Serif

Colors

Designer to choose colors to be used in the design.

Requirements
Must have
• Diversity in the cover- something eye catching. Photo on back cover. I'VE INCLUDED LINKS TO SOME EXAMPLES OF COVERS THAT I LIKE
Nice to have
• Designers have the flexibility to exert their creativity.I'VE INCLUDED LINKS TO SOME EXAMPLES OF COVERS THAT I LIKE
Should not have
• My picture on the cover

```html
<!DOCTYPE html>
<html lang="en">
<head>
<meta charset="utf-8">
<title>Things the Classroom Never Showed You — Book Cover</title>
<link rel="stylesheet" href="https://fonts.googleapis.com/css2?family=Source+Sans+3:wght@600;900&display=swap">
<style>
  :root {
    --paper: #ffffff;
    --ink: #2b2b2b;
    --orange: #efa020;
    --blue: #2188d1;
    --red: #e9203f;
    --suit-dark: #2a2f3d;
    --suit-mid: #6b7080;
    --suit-light: #c9ccd3;
  }
  * { margin: 0; padding: 0; box-sizing: border-box; }
  html, body {
    width: 776px;
    height: 1200px;
    overflow: hidden;
    background: var(--paper);
  }
  .cover {
    position: relative;
    width: 776px;
    height: 1200px;
    background: var(--paper);
    font-family: "Source Sans 3", "Source Sans Pro", Arial, sans-serif;
    text-align: center;
  }
  .title {
    position: absolute;
    top: 34px;
    left: 0;
    width: 100%;
    font-weight: 900;
    font-size: 92px;
    line-height: 0.9;
    letter-spacing: 1px;
    text-transform: uppercase;
  }
  .title span { display: block; }
  .title .tone-orange { color: var(--orange); }
  .title .tone-blue { color: var(--blue); }
  .title .tone-red { color: var(--red); }
  .subtitle {
    position: absolute;
    top: 500px;
    left: 60px;
    width: 656px;
    font-weight: 600;
    font-size: 24px;
    line-height: 1.3;
    color: var(--ink);
  }
  .team-photo {
    position: absolute;
    top: 612px;
    left: 36px;
    width: 706px;
    height: 420px;
  }
  .author {
    position: absolute;
    top: 1068px;
    left: 0;
    width: 100%;
    font-weight: 900;
    font-size: 68px;
    letter-spacing: 1px;
    color: var(--ink);
    text-transform: uppercase;
  }
</style>
</head>
<body>
  <main class="cover">
    <h1 class="title">
      <span class="tone-orange">Things the</span>
      <span class="tone-blue">Classroom</span>
      <span class="tone-blue">Never</span>
      <span class="tone-red">Showed</span>
      <span class="tone-red">You</span>
    </h1>
    <p class="subtitle">Unfiltered tips to help early career professionals successfully navigate the workplace</p>
    <svg class="team-photo" viewBox="0 0 706 420" role="img" aria-label="Photo of a diverse group of business professionals in suits standing in a V formation, led by a smiling young man in front">
      <defs>
        <linearGradient id="suits" x1="0" y1="0" x2="0" y2="1">
          <stop offset="0" stop-color="var(--suit-light)"/>
          <stop offset="0.35" stop-color="var(--suit-mid)"/>
          <stop offset="1" stop-color="var(--suit-dark)"/>
        </linearGradient>
      </defs>
      <polygon points="0,4 706,4 706,40 420,400 353,420 286,400 0,40" fill="url(#suits)"/>
    </svg>
    <p class="author">Dana Whitfield</p>
  </main>
</body>
</html>
```